New name flyer

We have just changed our business name from kR Property group to Harbour Lantern. We want to distribute a flyer to the local community to inform them of the change. We are a realestate agency which focuses mainly on property management but also sales. We service from Brisbane to the Sunshine coast.

Target Market(s)

Local community

Industry/Entity Type

realestate

Requirements
Must have
• Details of name change
Nice to have
• Servicing area Brisbane and Sunshine Coast, no change in management or services we offer, and will continue pride ourselves on offering a high level of service, with the same team from the Gold to Sunshine Coast.
Should not have
• too much wording.

```html
<!DOCTYPE html>
<html lang="en">
<head>
<meta charset="utf-8">
<title>Harbour Lantern – We Have Changed</title>
<link href="https://fonts.googleapis.com/css2?family=Jost:wght@400;600&family=Montserrat:wght@800&family=Rubik:wght@500;700&display=swap" rel="stylesheet">
<style>
  :root {
    --navy: #1d2f5e;
    --gold: #cf9b33;
    --white: #ffffff;
    --page: #b5b5b5;
    --photo-top: #5d5a63;
    --photo-mid: #8a7c74;
    --photo-pool: #6fa3ac;
  }
  * { margin: 0; padding: 0; box-sizing: border-box; }
  html, body { width: 1003px; height: 1200px; overflow: hidden; }
  body { background: var(--page); position: relative; }

  .flyer {
    position: absolute; left: 91px; top: 20px;
    width: 820px; height: 1160px;
    background: var(--navy);
    overflow: hidden;
  }
  .header-arrow { position: absolute; left: 0; top: 0; width: 820px; height: 260px; }

  .old-name {
    position: absolute; left: 40px; top: 128px;
    display: flex; align-items: center; gap: 10px;
    font-family: "Jost", sans-serif; font-weight: 600;
    font-size: 24px; color: var(--navy);
  }
  .old-name .mark { width: 22px; height: 22px; background: var(--navy); }

  .new-name {
    position: absolute; left: 452px; top: 110px; width: 340px;
    font-family: "Rubik", sans-serif; font-weight: 700;
    font-size: 40px; line-height: 1.1; letter-spacing: 1px;
    color: var(--white);
  }

  .headline-band {
    position: absolute; left: 0; top: 260px; width: 820px; height: 113px;
    background: var(--gold);
    display: flex; align-items: center; justify-content: center;
  }
  .headline {
    font-family: "Montserrat", sans-serif; font-weight: 800;
    font-size: 68px; color: var(--navy); letter-spacing: 0.5px;
  }

  .stripes { position: absolute; left: 0; top: 373px; width: 820px; height: 256px; }

  .message {
    position: absolute; left: 71px; top: 430px; width: 684px; height: 129px;
    border: 1px solid var(--navy);
  }
  .message-text {
    position: absolute; left: 0; right: 0; top: -18px;
    font-family: "Jost", sans-serif; color: var(--navy);
    text-align: center; line-height: 31px; font-size: 26px;
  }
  .message-text span { background: var(--white); padding: 0 6px; }
  .message-text .lead { font-weight: 600; font-size: 31px; }

  .property-photo {
    position: absolute; left: 0; top: 629px; width: 820px; height: 375px;
    background: linear-gradient(180deg, var(--photo-top) 0%, var(--photo-mid) 70%, var(--photo-pool) 100%);
  }

  .contact {
    position: absolute; left: 0; top: 1004px; width: 820px; height: 156px;
    display: flex; flex-direction: column; align-items: center; justify-content: center;
    font-family: "Rubik", sans-serif;
  }
  .phone {
    display: flex; align-items: center; gap: 6px;
    color: var(--white); font-weight: 700; font-size: 70px; line-height: 1;
  }
  .phone svg { width: 60px; height: 60px; }
  .website {
    margin-top: 10px; color: var(--gold); font-weight: 500; font-size: 38px; line-height: 1;
  }
</style>
</head>
<body>
  <main class="flyer">
    <svg class="header-arrow" viewBox="0 0 820 260" aria-hidden="true">
      <polygon points="0,59 300,59 300,15 414,156 340,260 0,260" fill="#ffffff"/>
    </svg>

    <div class="old-name"><span class="mark"></span>kR Property Group</div>
    <div class="new-name">HARBOUR<br>LANTERN</div>

    <div class="headline-band"><h1 class="headline">WE HAVE CHANGED</h1></div>

    <svg class="stripes" viewBox="0 0 820 256" aria-hidden="true">
      <polygon points="0,0 760,0 750,10 0,10" fill="#1d2f5e"/>
      <rect x="0" y="10" width="820" height="216" fill="#ffffff"/>
      <polygon points="82,226 820,226 820,241 68,241" fill="#1d2f5e"/>
      <rect x="0" y="241" width="820" height="15" fill="#cf9b33"/>
    </svg>

    <section class="message">
      <p class="message-text">
        <span>Servicing area Brisbane &amp; Sunshine Coast</span><br>
        <strong class="lead">No change in management or services</strong><br>
        we offer, &amp; will continue pride ourselves on<br>
        offering a high level of service, with the same<br>
        <span>team from the Gold to Sunshine Coast.</span>
      </p>
    </section>

    <div class="property-photo" role="img" aria-label="Photo of a modern two-storey home at dusk with a lit patio, outdoor dining set and pool"></div>

    <footer class="contact">
      <div class="phone">
        <svg viewBox="0 0 60 60" aria-hidden="true">
          <circle cx="30" cy="30" r="29" fill="#ffffff"/>
          <path d="M22 15c2-1 3 0 4 2l3 6c1 2 0 3-1 4l-2 2c1 4 5 8 9 9l2-2c1-1 2-2 4-1l6 3c2 1 3 2 2 4l-2 4c-2 2-5 3-9 1-9-4-16-11-19-20-2-5-1-8 1-10z" fill="#1d2f5e"/>
        </svg>
        <span>555-014-2290</span>
      </div>
      <div class="website">WWW.HARBOURLANTERN.COM</div>
    </footer>
  </main>
</body>
</html>
```